Postcard Design, half page postcard, double sided,

solar sales I want a half page. I like the color of the one attached. I want to do coupon sections with different offers Attached is one I started playing with, (double sided)
We had a guy working on it and then he stopped on Sunday and we have not heard form here. I have attached what he did. The building isn't what we wanted we wanted a house and the text isn't what we wanted either. We sent the designer the text requests and now no reply so who can finish it and then the back side is going to have a gift card on it.
Updates

Reason: last graphic designer disappeared.

Target Market(s)

sw usa

Industry/Entity Type

Coupon

Other font styles liked:
• Arial

Colors
d0dfed
0455a3
00a990
6b449b
ffffff

Requirements
Must have
• less is more. I dont want to drown them in information

```html
<!DOCTYPE html>
<html lang="en">
<head>
<meta charset="utf-8">
<title>Solar Power Event Postcard</title>
<link rel="stylesheet" href="https://fonts.googleapis.com/css2?family=Roboto+Condensed:wght@400;700&family=Open+Sans:wght@300;400;600&display=swap">
<style>
  :root {
    --blue: #0455a3;
    --blue-text: #1a5ea8;
    --teal: #00a990;
    --sky: #d0dfed;
    --white: #ffffff;
    --ink: #222222;
    --grey: #5a5a5a;
    --panel: #f1f2f4;
    --page: #e6e6e6;
  }
  * { margin: 0; padding: 0; box-sizing: border-box; }
  html, body { width: 863px; height: 1200px; overflow: hidden; }
  body { background: var(--page); position: relative; font-family: "Open Sans", Arial, sans-serif; }

  .card { position: absolute; left: 113px; width: 674px; overflow: hidden; box-shadow: 0 2px 8px rgba(0,0,0,.25); }
  .card--front { top: 56px; height: 527px; background: var(--panel); }
  .card--back { top: 603px; height: 517px; }

  .photo { position: absolute; }
  .front-photo { left: 0; top: 0; width: 674px; height: 196px;
    background: linear-gradient(180deg, #cfe1f2 0%, #b7d0e8 40%, #6f7c8c 62%, #6a5a52 100%); }
  .thumb-photo { left: 525px; top: 183px; width: 104px; height: 67px;
    background: linear-gradient(135deg, #e9e4dc, #8d7a66); border: 1px solid var(--white); z-index: 2; }

  .front-title { position: absolute; left: 0; width: 674px; text-align: center;
    font-family: "Roboto Condensed", Arial, sans-serif; font-weight: 700; }
  .front-title--main { top: 18px; font-size: 45px; line-height: 52px; color: var(--blue); letter-spacing: .5px; padding-left: 30px; }
  .front-title--sub { top: 70px; font-size: 31px; line-height: 36px; color: #2b2b2b; padding-left: 30px; }

  .offer-band { position: absolute; left: 0; top: 196px; width: 674px; height: 40px; background: var(--teal);
    color: var(--white); font-weight: 600; font-size: 20px; line-height: 40px; padding-left: 22px; }

  .evaluation-headline { position: absolute; left: 10px; top: 256px; width: 254px; text-align: center;
    font-family: "Roboto Condensed", Arial, sans-serif; font-weight: 700; font-size: 23px; line-height: 29px;
    color: var(--blue); text-transform: uppercase; }
  .evaluation-note { position: absolute; left: 10px; top: 385px; width: 254px; text-align: center;
    font-family: "Roboto Condensed", Arial, sans-serif; font-weight: 700; font-size: 21px; line-height: 28px; color: var(--grey); }

  .intro-copy { position: absolute; left: 316px; top: 266px; width: 326px; font-size: 11px; line-height: 17.4px;
    letter-spacing: -0.05px; color: #333; text-align: justify; }

  .front-footer { position: absolute; left: 0; top: 434px; width: 674px; height: 93px; }
  .perk-list { position: absolute; left: 14px; top: 444px; list-style: none;
    font-family: "Roboto Condensed", Arial, sans-serif; font-weight: 700; font-size: 16.5px; color: var(--white); }
  .perk-list li { height: 24px; line-height: 24px; display: flex; align-items: center; }
  .dot { width: 13px; height: 13px; border-radius: 50%; margin-right: 8px; flex: none;
    background: radial-gradient(circle at 35% 35%, #ffffff 0%, #c9c9c9 55%, #8a8a8a 100%); }
  .call-cta { position: absolute; left: 272px; top: 474px; font-size: 31px; line-height: 40px; font-weight: 300; color: var(--white); }
  .call-note { position: absolute; left: 457px; top: 478px; width: 205px; font-size: 13px; line-height: 19px; color: var(--white); }

  .back-photo { left: 0; top: 0; width: 674px; height: 517px;
    background: linear-gradient(180deg, #c9dcef 0%, #d6e4f2 35%, #b9cbe0 55%, #6c625d 72%, #4d4a4c 100%); }

  .hours-title { position: absolute; left: 27px; top: 31px; width: 236px; height: 27px; border-radius: 14px;
    background: var(--blue); color: var(--white); font-size: 16px; line-height: 27px; padding-left: 10px; }
  .hours-table { position: absolute; left: 30px; top: 62px; border-collapse: collapse; font-size: 15px; color: var(--ink); }
  .hours-table th, .hours-table td { text-align: left; height: 22px; padding: 0 3px; }
  .hours-table th { font-weight: 600; }
  .hours-table .day { width: 114px; }

  .benefit-list { position: absolute; left: 317px; top: 24px; list-style: none;
    font-weight: 600; font-size: 21.5px; color: var(--blue-text); }
  .benefit-list li { height: 37px; display: flex; align-items: center; }
  .benefit-list .dot { width: 18px; height: 18px; margin-right: 12px; }

  .qualify-band { position: absolute; left: 0; top: 484px; width: 674px; height: 30px; background: var(--blue);
    color: var(--white); font-size: 17px; line-height: 30px; padding-left: 24px; }
  .back-title { position: absolute; left: 310px; top: 466px; font-family: "Roboto Condensed", Arial, sans-serif;
    font-weight: 700; font-size: 37px; line-height: 44px; color: var(--white); text-shadow: 0 1px 3px rgba(0,0,0,.4); }
</style>
</head>
<body>

<section class="card card--front">
  <div class="photo front-photo" role="img" aria-label="Tiled house roof covered with solar panels under a blue sky"></div>
  <h1 class="front-title front-title--main">SOLAR POWER EVENT!</h1>
  <h2 class="front-title front-title--sub">Grab Your CHEAP Energy Today!</h2>
  <div class="offer-band">We Have Great Option That Will Save You Money!</div>
  <div class="photo thumb-photo" role="img" aria-label="Hands holding soil with a young green seedling"></div>

  <p class="evaluation-headline">Sumar is upon us. Now<br>is the time for a free,<br>no hassle solar<br>evaluation</p>
  <p class="evaluation-note">Its only tack a few minutes</p>

  <p class="intro-copy">we can answer your questions about solar, ask you a few questions about your home. then put together an easy to read chart that shows you clearly the saving you will recieve with solar. our no- nonsense straight forward approach will clearly show you if going solar is the best thing for you and your family. its not for everyone we understand that. give us the opportunity to explain how you can get solar on your home with zero out of pocket expense. its a lot easier that you may think. call us today to see if your home meets our pre-qualification guidelines.</p>

  <svg class="front-footer" viewBox="0 0 674 93" width="674" height="93" aria-hidden="true">
    <polygon points="0,0 267,0 230,93 0,93" fill="var(--blue)"/>
    <polygon points="253,38 674,38 674,93 230,93" fill="var(--teal)"/>
  </svg>
  <ul class="perk-list">
    <li><span class="dot"></span>Go Solar For $0 Down</li>
    <li><span class="dot"></span>Free Maintenance</li>
    <li><span class="dot"></span>Save A Ton Of $$$</li>
  </ul>
  <p class="call-cta">call us today</p>
  <p class="call-note">To see if your home meets our Pre-qualification guidelines.</p>
</section>

<section class="card card--back">
  <div class="photo back-photo" role="img" aria-label="Brick house with solar panels on the roof against a pale sky"></div>

  <div class="hours-title">House of opration</div>
  <table class="hours-table">
    <tr><th class="day">Day</th><th>Hours</th></tr>
    <tr><td class="day">Monday</td><td>9:00am - 5:00pm</td></tr>
    <tr><td class="day">Tuesday</td><td>9:00am - 5:00pm</td></tr>
    <tr><td class="day">Wednesday</td><td>9:00am - 5:00pm</td></tr>
    <tr><td class="day">Thursday</td><td>9:00am - 7:00pm</td></tr>
    <tr><td class="day">Friday</td><td>9:00am - 7:00pm</td></tr>
    <tr><td class="day">Saturday</td><td>9:00am - 8:00pm</td></tr>
    <tr><td class="day">Sunday</td><td>Closed</td></tr>
  </table>

  <ul class="benefit-list">
    <li><span class="dot"></span>Ownership In 12 Year</li>
    <li><span class="dot"></span>Zero Out Of Pocket</li>
    <li><span class="dot"></span>Hugh Federal Incentives</li>
    <li><span class="dot"></span>Free Evaluation</li>
    <li><span class="dot"></span>No Hard Selling</li>
  </ul>

  <div class="qualify-band">NOT ALL HOMES WILL QUALIFY</div>
  <p class="back-title">SOLAR POWER EVENT!</p>
</section>

</body>
</html>
```